Small Unique Manufacturer Needs a facelift for eCommerce Wordpress Site

We need a wordpress template design that brands our business based in Minneapolis, MN called "Lantern Socials". Lantern Socials manufacturers and assembles fraternity and sorority paddle kits for Sisterhood parties and fraternity rush and pledge process decoration parties. We're our site is an eCommerce site that runs at LanternSocials.example. We'd like an attractive design that's more on the feminine side (rather than masculine) as our primary consumer will be female. However as we move into the future we will have products for the fraternities as well.
We like earthy neutral colors, our products are unfinished pine, walnut, and oak, but we're not keen on focusing on woodgrain designs, etc.
The final design should communicate fun, be clean, clear, and bright, and appeal to the millennial generation and must be fully functional.
We're currently using the CartWillow plugin for our eCommerce back end and like it.

Target Market(s)

College greeks. Fraternity and Sorority Members

Industry/Entity Type

Business

Font styles to use
Sans Serif

Colors
cde8f3
ecf7fa
f9d9e8
fbc994

Requirements
Must have
• Clean, clear design. A nice branding project start to finish. Millennial focus.
• Must work with our current CartWillow page.
Should not have
• Anything that looks down or talks down to college students.

```html
<!DOCTYPE html>
<html lang="en">
<head>
<meta charset="utf-8">
<title>Lantern Socials — Paddle Kits</title>
<link href="https://fonts.googleapis.com/css2?family=Open+Sans:wght@300;400;600&display=swap" rel="stylesheet">
<style>
:root{
  --peach:#fbc994;
  --sky:#cde8f3;
  --sky-light:#ecf7fa;
  --page:#f3f3f2;
  --ink:#3d3d3d;
  --grey-card:#ececec;
  --logo:#6a6a6a;
}
*{box-sizing:border-box;margin:0;padding:0}
html,body{width:941px;height:1200px;overflow:hidden}
body{position:relative;background:var(--page);font-family:"Open Sans",Arial,sans-serif;color:var(--ink)}
.abs{position:absolute}
a{color:inherit;text-decoration:none}

.top-rule{left:0;top:0;width:941px;height:3px;background:var(--peach)}
.header{left:0;top:3px;width:941px;height:85px;background:#fff}
.account-links{left:622px;top:4px;width:215px;height:24px;background:var(--peach);display:flex;align-items:center;justify-content:space-around;font-size:9.6px;color:#555;padding:0 4px}
.account-links span+span{border-left:1px solid #f0b879}
.account-links span{padding:0 4px}
.brand{left:102px;top:36px;font-size:29px;font-weight:300;letter-spacing:.5px;color:var(--logo)}
.search{left:663px;top:50px;width:172px;height:19px;border:1px solid #cfcfcf;border-radius:3px;background:#fff;font-size:8px;font-style:italic;color:#999;padding:3px 7px}
.search svg{position:absolute;right:6px;top:3px}

.nav{left:0;top:88px;width:941px;height:35px;background:linear-gradient(#dcedf5,var(--sky))}
.nav-list{left:98px;top:97px;display:flex;gap:13px;font-size:13.6px;color:#555}
.nav-list a{padding:0 3px;line-height:19px}
.nav-list .current{background:#fff;border-radius:2px;color:#444}
.basket{left:689px;top:98px;font-size:10.4px;color:#444}
.basket-icon{left:813px;top:94px}

.hero{left:102px;top:142px;width:735px;height:314px;background:#dcdcdc;padding:5px}
.hero-photo{width:100%;height:100%;background:
  radial-gradient(ellipse 40% 70% at 72% 52%,rgba(120,78,40,.45),transparent 70%),
  linear-gradient(100deg,#f6f3ee 0%,#e8dccd 20%,#d2b796 40%,#c9a985 65%,#c4a482 100%)}
.caption{left:133px;top:198px;width:245px;height:200px;background:linear-gradient(90deg,rgba(52,52,52,.93),rgba(70,70,70,.88));color:#fff;padding:16px 0 0 23px}
.caption h1{font-size:25px;font-weight:400;color:#eef6f8;line-height:30px}
.caption p{margin-top:7px;font-size:12.8px;line-height:18.4px;padding-left:2px}
.btn-shop{left:161px;top:344px;width:76px;height:30px;background:var(--peach);color:#444;font-size:13px;display:flex;align-items:center;justify-content:center;border-radius:2px}
.hero-arrows{left:332px;top:370px;display:flex;gap:1px}
.hero-arrows span{width:22px;height:28px;background:#1f1f1f;display:flex;align-items:center;justify-content:center}

.category{top:473px;width:173px;height:189px;border:1px solid #ddd;background:var(--peach)}
.category .thumb{height:155px;background:
  radial-gradient(ellipse 22% 55% at 55% 50%,rgba(190,130,55,.75),transparent 75%),
  linear-gradient(135deg,#bdb4a8,#a69c8f 50%,#b5ab9f)}
.category .label{height:33px;display:flex;align-items:center;justify-content:center;font-size:16px;font-weight:600;color:#4a3b2c}

.featured-bar{left:102px;top:687px;width:735px;height:31px;background:var(--sky);border-radius:3px;font-size:13.6px;font-weight:600;color:#333;padding:5px 9px}
.featured-arrows{left:800px;top:694px}

.product{top:727px;width:175px;height:256px;background:var(--grey-card);border:1px solid #dcdcdc}
.product .shot{position:absolute;left:15px;top:14px;width:142px;height:134px;background:#fff;border:2px solid #cfcfcf;display:flex;align-items:center;justify-content:center}
.product .shot div{width:110px;height:112px;background:radial-gradient(ellipse 30% 55% at center,#d39d4e 0%,#e6c58a 50%,#fff 100%)}
.product h3{position:absolute;left:13px;top:161px;font-size:13.6px;font-weight:600;color:#444}
.product p{position:absolute;left:14px;top:183px;font-size:10.4px;line-height:14.4px;color:#444}
.product .price{position:absolute;left:15px;top:222px;font-size:13.5px;font-weight:600;color:#333}
.product .add{position:absolute;left:97px;top:220px;width:58px;height:23px;background:var(--peach);font-size:9.6px;display:flex;align-items:center;justify-content:center;color:#444;border-radius:2px}

.footer{left:0;top:1014px;width:941px;height:143px;background:var(--sky);border-top:1px solid #bfdceb;border-bottom:1px solid #bfdceb}
.foot-head{font-size:12.5px;color:#333}
.about{left:212px;top:1030px;width:200px}
.about p{margin-top:10px;font-size:8.8px;line-height:16.8px;color:#444}
.links{left:443px;top:1030px}
.links ul{list-style:none;margin-top:8px;margin-left:3px;font-size:8.8px;line-height:16px;color:#444}
.newsletter{left:583px;top:1030px}
.email{left:584px;top:1058px;width:146px;height:16px;background:var(--sky-light);border-radius:2px;font-size:6.5px;font-style:italic;color:#888;padding:4px 9px}
.follow{left:584px;top:1090px;font-size:12.5px;color:#333}
.socials{left:586px;top:1110px;display:flex;gap:6px}
.socials span{width:19px;height:19px;border-radius:2px}

.copyright{left:102px;top:1171px;font-size:9px;color:#666}
.cards{left:709px;top:1172px;display:flex;gap:4px}
.cards span{width:22px;height:14px;border-radius:2px;border:1px solid #d0d0d0}
</style>
</head>
<body>
<div class="abs header"></div>
<div class="abs top-rule"></div>
<nav class="abs account-links"><span>Account</span><span>Wishlist</span><span>Help</span><span>Log in</span><span>Sign up</span></nav>
<div class="abs brand">YOURLOGO</div>
<div class="abs search">Search entire store...
  <svg width="11" height="11" viewBox="0 0 11 11"><circle cx="4.5" cy="4.5" r="3.2" fill="none" stroke="#2b5f8a" stroke-width="1.6"/><line x1="7" y1="7" x2="10" y2="10" stroke="#2b5f8a" stroke-width="2"/></svg>
</div>

<div class="abs nav"></div>
<nav class="abs nav-list">
  <a class="current">Home</a><a>About Us</a><a>Our Products</a><a>View Gallery</a><a>Contact Us</a>
</nav>
<div class="abs basket">Your basket ($0 items)</div>
<svg class="abs basket-icon" width="22" height="18" viewBox="0 0 22 18"><path d="M6 7 L11 1 L16 7" fill="none" stroke="#555" stroke-width="1.6"/><path d="M1 7 H21 L18 17 H4 Z" fill="#555"/></svg>

<section class="abs hero">
  <div class="hero-photo" role="img" aria-label="Three engraved wooden paddles on a warm textured backdrop"></div>
</section>
<div class="abs caption">
  <h1>Lorem Ipsum</h1>
  <p>Lorem ipsum is dummy text<br>only dolor sit amet, consec<br>tetur adipisicing elit, sed do<br>eiusmod tempor inci.</p>
</div>
<a class="abs btn-shop">Shop Now</a>
<div class="abs hero-arrows">
  <span><svg width="8" height="12" viewBox="0 0 8 12"><path d="M6 1 L2 6 L6 11" fill="none" stroke="#fff" stroke-width="2"/></svg></span>
  <span><svg width="8" height="12" viewBox="0 0 8 12"><path d="M2 1 L6 6 L2 11" fill="none" stroke="#fff" stroke-width="2"/></svg></span>
</div>

<div class="abs category" style="left:102px"><div class="thumb" role="img" aria-label="Engraved wooden paddle on linen"></div><div class="label">Lorem Ipsum</div></div>
<div class="abs category" style="left:290px"><div class="thumb" role="img" aria-label="Engraved wooden paddle on linen"></div><div class="label">Lorem Ipsum</div></div>
<div class="abs category" style="left:477px"><div class="thumb" role="img" aria-label="Engraved wooden paddle on linen"></div><div class="label">Lorem Ipsum</div></div>
<div class="abs category" style="left:665px"><div class="thumb" role="img" aria-label="Engraved wooden paddle on linen"></div><div class="label">Lorem Ipsum</div></div>

<div class="abs featured-bar">Featured Products</div>
<svg class="abs featured-arrows" width="30" height="16" viewBox="0 0 30 16"><path d="M10 2 L4 8 L10 14" fill="none" stroke="#f3b070" stroke-width="2.2"/><path d="M20 2 L26 8 L20 14" fill="none" stroke="#f3b070" stroke-width="2.2"/></svg>

<article class="abs product" style="left:100px"><div class="shot"><div role="img" aria-label="Wooden paddle product photo"></div></div><h3>Product Name Here</h3><p>Lorem ipsum dolor sit amet,<br>consectetur adipisicing kur.</p><span class="price">$58.50</span><a class="add">Add to cart</a></article>
<article class="abs product" style="left:288px"><div class="shot"><div role="img" aria-label="Wooden paddle product photo"></div></div><h3>Product Name Here</h3><p>Lorem ipsum dolor sit amet,<br>consectetur adipisicing kur.</p><span class="price">$58.50</span><a class="add">Add to cart</a></article>
<article class="abs product" style="left:475px"><div class="shot"><div role="img" aria-label="Wooden paddle product photo"></div></div><h3>Product Name Here</h3><p>Lorem ipsum dolor sit amet,<br>consectetur adipisicing kur.</p><span class="price">$58.50</span><a class="add">Add to cart</a></article>
<article class="abs product" style="left:663px"><div class="shot"><div role="img" aria-label="Wooden paddle product photo"></div></div><h3>Product Name Here</h3><p>Lorem ipsum dolor sit amet,<br>consectetur adipisicing kur.</p><span class="price">$58.50</span><a class="add">Add to cart</a></article>

<footer class="abs footer"></footer>
<div class="abs about"><div class="foot-head">About Our Company</div><p>Lorem ipsum dolor sit amet,<br>consectetur adipisicing elit, sed do<br>eiusmod tempor incididunt ut labore et<br>dolore magna aliqua. Ut enim ad minim<br>veniam, quis nostrud exercitation.</p></div>
<div class="abs links"><div class="foot-head">Quick Links</div><ul><li>Home</li><li>About Us</li><li>Our Products</li><li>View Gallery</li><li>Contact Us</li></ul></div>
<div class="abs newsletter foot-head">Sign Up to our Newsletter</div>
<div class="abs email">Enter your Email</div>
<div class="abs follow">Follow Us On:</div>
<div class="abs socials"><span style="background:#e8692e"></span><span style="background:#1fa1e0"></span><span style="background:#3b5a9a"></span><span style="background:#4a6f93"></span></div>

<div class="abs copyright">Copyright©lanternsocials.2014. All rights reserved</div>
<div class="abs cards"><span style="background:#e9eef5"></span><span style="background:#f4ece2"></span><span style="background:#e3eef8"></span><span style="background:#f2f2f2"></span><span style="background:#eaf0f7"></span></div>
</body>
</html>
```